Football blog needs a Wordpress design new site

We need a wordpress design for a new football blog site. We would like to see a design that uses the colours green, white and black and one that makes good use of the slideshow widgets as scene in the site 'www.trenvix.net'
We would like a modern and sleek looking site but one that is also professional and easy to navigate.
Unfortunately due to unforeseen circumstances we are having to shorten the deadline date for this project.
The new deadline date is 16/07/2014.
We apologise for any inconveniance
It Professional

```html
<!DOCTYPE html>
<html lang="en">
<head>
<meta charset="utf-8">
<title>Sideline Chatter – Football Blog</title>
<link href="https://fonts.googleapis.com/css2?family=Lato:ital,wght@0,300;0,400;0,700;1,400;1,700&display=swap" rel="stylesheet">
<style>
:root{
  --green:#3dbb4d;
  --green-dark:#2f9a3d;
  --ink:#222;
  --bar:#2b2b2b;
  --footer:#232323;
  --page:#f1f1f1;
  --card:#ffffff;
  --muted:#7a7a7a;
  --line:#cfcfcf;
  --tag-dark:#2a2a2a;
  --tag-gold:#d9a21b;
}
*{box-sizing:border-box;margin:0;padding:0}
html,body{width:1200px;height:2707px;overflow:hidden}
body{background:var(--page);font-family:'Lato',sans-serif;color:var(--ink);position:relative}
.abs{position:absolute}
.ph{position:absolute;display:block}

/* header */
.brand-mark{left:128px;top:22px;width:96px;height:96px;border-radius:50%;background:var(--green)}
.social{right:81px;top:26px;display:flex;gap:8px}
.social span{width:27px;height:27px;border-radius:50%;background:#9ea3b3;display:block}
.search{left:897px;top:78px;width:222px;height:32px;border-bottom:1px solid var(--line);font-size:13px;font-style:italic;color:#999;padding:8px 20px}
.search-btn{right:81px;top:80px;width:26px;height:26px;border-radius:50%;background:var(--green)}
.search-btn svg{position:absolute;left:6px;top:6px}

/* nav */
.nav{left:0;top:126px;width:1200px;height:55px;background:var(--bar)}
.nav-brand{left:56px;top:126px;width:228px;height:55px;background:#fff;clip-path:polygon(0 0,100% 0,93% 100%,7% 100%)}
.nav-brand b{position:absolute;left:44px;top:16px;font-size:21px;font-weight:700;color:var(--green);letter-spacing:-.3px}
.nav ul{list-style:none}
.nav li{position:absolute;top:0;height:55px;line-height:55px;color:#d8d8d8;font-size:19px;font-style:italic;font-weight:400}
.nav li.active{background:var(--green);color:#fff;font-weight:700;padding:0 28px;clip-path:polygon(7% 0,100% 0,93% 100%,0 100%)}
.nav .sep{position:absolute;top:10px;width:1px;height:35px;background:#444;transform:skewX(-14deg)}

/* slider */
.slide{overflow:hidden}
.slide .caption{position:absolute;left:0;bottom:0;width:100%;height:56px;background:rgba(20,20,20,.72);color:#fff;font-weight:300;font-size:28px;line-height:56px;padding-left:20px;white-space:nowrap;overflow:hidden}
.slide.small .caption{height:46px;line-height:46px;font-size:23px}
.tags{position:absolute;left:20px;display:flex;gap:6px}
.tag{font-size:10px;font-weight:700;text-transform:uppercase;color:#fff;padding:4px 8px;background:var(--green)}
.tag.dark{background:var(--tag-dark)}
.tag.gold{background:var(--tag-gold)}

/* section headings */
.sec-title{position:absolute;font-size:20px;font-weight:700;color:#222;display:flex;align-items:center}
.sec-title::after{content:"";height:1px;background:linear-gradient(90deg,#555,var(--green));margin-left:6px;flex:1}
.arrows{position:absolute;display:flex;gap:3px}
.arrows svg{display:block}

/* top events */
.event{position:absolute;top:731px;width:237px;height:329px;background:var(--card)}
.event .ph{left:0;top:0;width:237px;height:157px}
.date{position:absolute;left:0;top:91px;width:60px;height:63px;background:var(--green);color:#fff;text-align:center}
.date b{display:block;font-size:30px;font-weight:400;line-height:34px;margin-top:6px}
.date small{font-size:12px;display:block;opacity:.85}
.event h3{position:absolute;left:20px;top:180px;width:200px;font-size:18px;font-weight:400;font-style:italic;line-height:24px}
.event h3.hl{color:var(--green)}
.event p{position:absolute;left:20px;top:248px;width:200px;font-size:13px;line-height:24px;color:var(--muted)}

/* video */
.play{position:absolute;left:79px;top:53px;width:50px;height:44px;background:var(--green)}
.play svg{position:absolute;left:17px;top:12px}

/* topics */
.topic{position:absolute;top:1332px;width:211px;height:268px;background:var(--card)}
.topic .ph{left:0;top:0;width:211px;height:121px}
.topic h4{position:absolute;left:10px;top:140px;font-size:15px;font-weight:400;color:#222}
.topic h4.hl{color:var(--green)}
.topic p{position:absolute;left:10px;top:166px;width:195px;font-size:12.5px;line-height:20px;color:var(--muted)}
.topic .meta{position:absolute;left:10px;top:238px;font-size:12px;font-style:italic;color:#333}
.topic .meta a{color:inherit;text-decoration:none;margin-right:40px}
.topic .meta a.hl{color:var(--green);text-decoration:underline}

/* news list */
.news{position:absolute;left:800px;width:319px;height:96px;background:var(--card)}
.news .ph{top:0;width:112px;height:92px}
.news .txt{position:absolute;top:12px;width:190px}
.news .d{font-size:12px;font-style:italic;color:#333}
.news .t{font-size:13px;color:var(--green);margin-top:8px}
.news .r{font-size:11px;font-style:italic;color:#999;margin-top:12px}

/* popular */
.tile{position:absolute;overflow:hidden}
.tile .caption{position:absolute;left:0;bottom:0;width:100%;height:44px;background:rgba(20,20,20,.78);color:#fff;font-size:20px;font-weight:300;line-height:44px;padding-left:16px}
.tile .caption.hl{color:var(--green)}
.tile .tags{top:10px;left:16px}

/* banter column */
.feature-meta{position:absolute;left:81px;top:2320px;font-size:13px;color:#333;text-transform:uppercase}
.feature-meta span{margin-left:36px}
.feature-title{position:absolute;left:81px;top:2346px;width:330px;font-size:19px;color:var(--green);line-height:24px}
.feature-tags{position:absolute;left:81px;top:2410px;display:flex;gap:6px}
.feature-text{position:absolute;left:81px;top:2446px;width:320px;font-size:12.5px;line-height:22px;color:#888}
.post{position:absolute;left:430px;width:328px;height:88px}
.post .ph{left:0;top:0;width:96px;height:86px}
.post h5{position:absolute;left:106px;top:4px;width:220px;font-size:16px;font-weight:400;line-height:21px;color:#222}
.post h5.hl{color:var(--green)}
.post .by{position:absolute;left:106px;top:65px;font-size:12px;color:#333;text-transform:uppercase}

/* ad */
.ad{left:800px;top:2096px;width:319px;height:196px;background:linear-gradient(135deg,#1a62b8,#0b2f6b)}
.ad h6{position:absolute;right:14px;top:14px;font-size:27px;font-weight:700;color:#fff;line-height:28px;text-align:right;text-transform:uppercase;letter-spacing:-.5px}
.ad small{position:absolute;right:16px;top:82px;font-size:20px;font-weight:700;color:#fff}
.ad .console{position:absolute;left:12px;top:72px;width:110px;height:110px;background:#111;border-radius:4px}

/* footer */
.footer{left:0;top:2514px;width:1200px;height:193px;background:var(--footer)}
.crumbs{position:absolute;left:81px;top:32px;font-size:13px;color:#aaa}
.crumbs a{color:inherit;text-decoration:none}
.crumbs a.hl{color:var(--green)}
.foot-brand{position:absolute;left:81px;top:84px;font-size:21px;font-weight:700;color:#555}
.foot-mark{position:absolute;left:252px;top:72px;width:70px;height:70px;border-radius:50%;background:#3a3a3a}
.copy{position:absolute;left:81px;top:126px;font-size:12.5px;color:#999}
.fcol{position:absolute;top:32px;list-style:none}
.fcol li{font-size:13px;color:#aaa;height:37.5px;padding-left:14px;position:relative}
.fcol li::before{content:"";position:absolute;left:0;top:6px;width:6px;height:6px;background:#555}
.fcol li.hl{color:var(--green)}
.fcol li.hl::before{background:var(--green)}
</style>
</head>
<body>

<header>
  <div class="abs brand-mark"></div>
  <div class="abs social" aria-label="Social links">
    <span></span><span></span><span></span><span></span><span></span><span></span>
  </div>
  <div class="abs search">Search</div>
  <div class="abs search-btn"><svg width="14" height="14" viewBox="0 0 14 14"><circle cx="6" cy="6" r="4.5" fill="none" stroke="#fff" stroke-width="2"/><line x1="9.5" y1="9.5" x2="13" y2="13" stroke="#fff" stroke-width="2"/></svg></div>
</header>

<nav class="abs nav">
  <ul>
    <li class="active" style="left:283px">Home</li>
    <li style="left:395px">About Us</li>
    <li style="left:514px">World Cup</li>
    <li style="left:644px">Top Banter</li>
    <li style="left:776px">Videos</li>
    <li style="left:874px">Pug Quiz</li>
    <li style="left:991px">Competitions</li>
  </ul>
  <i class="sep" style="left:500px"></i><i class="sep" style="left:628px"></i><i class="sep" style="left:760px"></i><i class="sep" style="left:858px"></i><i class="sep" style="left:974px"></i>
</nav>
<div class="abs nav-brand"><b>Sideline Chatter</b></div>

<section class="slider">
  <div class="ph slide" style="left:0;top:186px;width:76px;height:478px;background:linear-gradient(180deg,#3b4c6b,#c9cfd8 60%,#2a2a2a)" role="img" aria-label="Football player in white kit"><div class="caption" style="font-size:26px;padding-left:0">014</div></div>
  <div class="ph slide" style="left:81px;top:186px;width:515px;height:478px;background:linear-gradient(160deg,#1d3f7a,#2b6fb4 45%,#c2a37c 75%,#3c2a22)" role="img" aria-label="Fans in blue shirts cheering in a stadium">
    <div class="tags" style="top:388px"><span class="tag">Top Sideline</span><span class="tag dark">Lifestyle</span></div>
    <div class="caption">Lorem ipsum dolor sit amet consec</div>
  </div>
  <div class="ph slide small" style="left:601px;top:186px;width:518px;height:237px;background:linear-gradient(135deg,#3a3a3a,#b48c6e 50%,#d8c3a0)" role="img" aria-label="Two fans smiling in the stands">
    <div class="tags" style="top:158px"><span class="tag">Top Sideline</span><span class="tag dark">Lifestyle</span></div>
    <div class="caption">Argentina fans get set to cheer their team against</div>
  </div>
  <div class="ph slide small" style="left:601px;top:428px;width:518px;height:236px;background:linear-gradient(135deg,#3a2a1a,#b52a22 45%,#c99a2a 70%,#2a1f1a)" role="img" aria-label="Team in red celebrating with a trophy">
    <div class="tags" style="top:158px"><span class="tag">Top Sideline</span><span class="tag dark">Recap</span><span class="tag gold">Woldcup</span></div>
    <div class="caption">Lorem ipsum dolor sit amet consec</div>
  </div>
  <div class="ph slide small" style="left:1124px;top:186px;width:76px;height:478px;background:linear-gradient(180deg,#2a2a2a,#b8902a 40%,#3a2a10)" role="img" aria-label="Golden trophy close-up">
    <div class="tags" style="top:350px;left:10px"><span class="tag">Top</span></div>
    <div class="caption" style="padding-left:14px">Cup w</div>
  </div>
</section>

<!-- Top events -->
<h2 class="sec-title" style="left:81px;top:694px;width:1006px">Top Events</h2>
<div class="arrows" style="left:1091px;top:702px"><svg width="10" height="12"><path d="M8 1 3 6l5 5" fill="none" stroke="#333" stroke-width="2"/></svg><svg width="10" height="12"><path d="M2 1l5 5-5 5" fill="none" stroke="#3dbb4d" stroke-width="2"/></svg></div>

<article class="event" style="left:81px"><span class="ph" style="background:linear-gradient(135deg,#3a6a2a,#8aa0c8,#2a4a8a)" role="img" aria-label="Players challenging for the ball"></span><div class="date"><b>30</b><small>APR</small></div><h3 class="hl">Lorem ipsum dolor sit amet dolor</h3><p>Consectetur adipis Maecenas aliquet velit in lacus porta, dignissim elementu.</p></article>
<article class="event" style="left:348px"><span class="ph" style="background:linear-gradient(135deg,#4a7a3a,#c8d4e0,#7aa0c8)" role="img" aria-label="Player lying on the pitch"></span><div class="date"><b>30</b><small>APR</small></div><h3>Lorem ipsum dolor sit amet dolor</h3><p>Consectetur adipis Maecenas aliquet velit in lacus porta, dignissim elementu.</p></article>
<article class="event" style="left:615px"><span class="ph" style="background:linear-gradient(135deg,#3f8a3a,#dcdcdc,#4a8a3a)" role="img" aria-label="Players running on a green pitch"></span><div class="date"><b>30</b><small>APR</small></div><h3>Lorem ipsum dolor sit amet dolor</h3><p>Consectetur adipis Maecenas aliquet velit in lacus porta, dignissim elementu.</p></article>
<article class="event" style="left:881px"><span class="ph" style="background:linear-gradient(135deg,#4a8a3a,#e0e0e0,#c8a030)" role="img" aria-label="Two players in a tackle"></span><div class="date"><b>30</b><small>APR</small></div><h3>Lorem ipsum dolor sit amet dolor</h3><p>Consectetur adipis Maecenas aliquet velit in lacus porta, dignissim elementu.</p></article>

<!-- Latest video -->
<h2 class="sec-title" style="left:81px;top:1086px;width:644px">Latest Video</h2>
<div class="arrows" style="left:730px;top:1094px"><svg width="10" height="12"><path d="M8 1 3 6l5 5" fill="none" stroke="#333" stroke-width="2"/></svg><svg width="10" height="12"><path d="M2 1l5 5-5 5" fill="none" stroke="#3dbb4d" stroke-width="2"/></svg></div>
<div class="ph" style="left:81px;top:1121px;width:211px;height:151px;background:linear-gradient(135deg,#2a3a1a,#5a6a2a,#1a2a12)" role="img" aria-label="Video still of a match"><div class="play"><svg width="16" height="20"><path d="M0 0l16 10L0 20z" fill="#1a1a1a"/></svg></div></div>
<div class="ph" style="left:316px;top:1121px;width:211px;height:151px;background:linear-gradient(135deg,#3a8a3a,#d8c030,#2a7a2a)" role="img" aria-label="Player in yellow on the ball"></div>
<div class="ph" style="left:548px;top:1121px;width:210px;height:151px;background:linear-gradient(135deg,#2a8a3a,#e0c020,#1a4a9a)" role="img" aria-label="Green and yellow flag with a trophy"></div>

<!-- Latest topics -->
<h2 class="sec-title" style="left:81px;top:1297px;width:644px">Latest Topics</h2>
<div class="arrows" style="left:730px;top:1305px"><svg width="10" height="12"><path d="M8 1 3 6l5 5" fill="none" stroke="#333" stroke-width="2"/></svg><svg width="10" height="12"><path d="M2 1l5 5-5 5" fill="none" stroke="#3dbb4d" stroke-width="2"/></svg></div>
<article class="topic" style="left:81px"><span class="ph" style="background:linear-gradient(135deg,#c83a2a,#e0c030,#2a8a4a)" role="img" aria-label="Colourful crowd of fans"></span><h4 class="hl">Lorem ipsum dolor sit amet,</h4><p>Consectetur adipisc Maecenas aliquet velit in lacus consectetur adipiscing elit.</p><div class="meta"><a class="hl">3 Comment</a><a>Read more</a></div></article>
<article class="topic" style="left:316px"><span class="ph" style="background:linear-gradient(135deg,#1a1a2a,#8a7a5a,#2a2a3a)" role="img" aria-label="Street celebration at night"></span><h4>Lorem ipsum dolor sit amet,</h4><p>Consectetur adipisc Maecenas aliquet velit in lacus consectetur adipiscing elit.</p><div class="meta"><a>3 Comment</a><a>Read more</a></div></article>
<article class="topic" style="left:548px"><span class="ph" style="background:linear-gradient(135deg,#2a7a3a,#e0c830,#3a8a4a)" role="img" aria-label="Team in yellow lining up"></span><h4>Lorem ipsum dolor sit amet,</h4><p>Consectetur adipisc Maecenas aliquet velit in lacus consectetur adipiscing elit.</p><div class="meta"><a>3 Comment</a><a>Read more</a></div></article>

<!-- Latest news -->
<h2 class="sec-title" style="left:800px;top:1086px">Latest News</h2>
<div class="news" style="top:1121px"><span class="ph" style="left:0;background:linear-gradient(135deg,#3a7a3a,#2a3a8a,#a02a3a)" role="img" aria-label="Player in striped kit"></span><div class="txt" style="left:150px"><div class="d">JUL 10, 2014</div><div class="t">Lorem ipsum dolor amet</div><div class="r">Read more</div></div></div>
<div class="news" style="top:1217px"><div class="txt" style="left:16px"><div class="d">JUL 10, 2014</div><div class="t">Lorem ipsum dolor amet</div><div class="r">Read more</div></div><span class="ph" style="right:0;background:linear-gradient(135deg,#4a8a3a,#e8e8e8,#3a6a2a)" role="img" aria-label="Player in white kit"></span></div>
<div class="news" style="top:1313px"><div class="txt" style="left:16px"><div class="d">JUL 10, 2014</div><div class="t">Lorem ipsum dolor amet</div><div class="r">Read more</div></div><span class="ph" style="right:0;background:linear-gradient(135deg,#4a8a3a,#c83a3a,#e0e0e0)" role="img" aria-label="Player in red and white stripes"></span></div>
<div class="news" style="top:1409px"><div class="txt" style="left:16px"><div class="d">JUL 10, 2014</div><div class="t">Lorem ipsum dolor amet</div><div class="r">Read more</div></div><span class="ph" style="right:0;background:linear-gradient(135deg,#1a1a2a,#8a3a6a,#3a3a5a)" role="img" aria-label="Night match action"></span></div>
<div class="news" style="top:1505px"><div class="txt" style="left:16px"><div class="d">JUL 10, 2014</div><div class="t">Lorem ipsum dolor amet</div><div class="r">Read more</div></div><span class="ph" style="right:0;background:linear-gradient(135deg,#3a7a3a,#c83a2a,#e0c030)" role="img" aria-label="Players competing for the ball"></span></div>

<!-- Most popular -->
<h2 class="sec-title" style="left:81px;top:1628px;width:644px">Most Popular</h2>
<div class="arrows" style="left:730px;top:1636px"><svg width="10" height="12"><path d="M8 1 3 6l5 5" fill="none" stroke="#333" stroke-width="2"/></svg><svg width="10" height="12"><path d="M2 1l5 5-5 5" fill="none" stroke="#3dbb4d" stroke-width="2"/></svg></div>
<div class="tile" style="left:81px;top:1662px;width:329px;height:188px;background:linear-gradient(135deg,#2a8a3a,#e0c030,#c87a3a)" role="img" aria-label="Carnival dancers in colourful costumes"><div class="tags"><span class="tag">Top Sideline</span><span class="tag dark">Lifestyle</span></div><div class="caption hl">Lorem ipsum dolor sit amet</div></div>
<div class="tile" style="left:430px;top:1662px;width:328px;height:188px;background:linear-gradient(135deg,#1a4a9a,#7aa8d8,#2a5aa0)" role="img" aria-label="Supporter with painted face"><div class="tags"><span class="tag">Top Sideline</span><span class="tag dark">Recap</span><span class="tag gold">Woldcup</span></div><div class="caption">Argentina Fans Rejoice</div></div>
<div class="tile" style="left:81px;top:1870px;width:329px;height:188px;background:linear-gradient(135deg,#2a7a3a,#e8d040,#c89a7a)" role="img" aria-label="Fan with a flag"><div class="tags"><span class="tag">Top Sideline</span><span class="tag dark">Lifestyle</span></div><div class="caption">Top 10 World Cup WAGs</div></div>
<div class="tile" style="left:430px;top:1870px;width:328px;height:188px;background:linear-gradient(135deg,#0e3a5a,#2a8a9a,#c8b090)" role="img" aria-label="Presenters on a studio stage"><div class="tags"><span class="tag">Top Sideline</span><span class="tag gold">Woldcup</span></div><div class="caption">Things Ray got totally Wrong</div></div>

<!-- The Bollocks -->
<h2 class="sec-title" style="left:800px;top:1628px">The Bollocks</h2>
<div class="news" style="top:1662px"><span class="ph" style="left:0;background:linear-gradient(135deg,#1a4a9a,#3a8a3a,#e0e0e0)" role="img" aria-label="Players celebrating"></span><div class="txt" style="left:150px"><div class="t" style="margin-top:0">Lorem ipsum dolor amet</div><div class="d" style="margin-top:8px">JUL 10, 2014</div><div class="r">Read more</div></div></div>
<div class="news" style="top:1758px"><div class="txt" style="left:16px"><div class="t" style="margin-top:0">Lorem ipsum dolor amet</div><div class="d" style="margin-top:8px">JUL 10, 2014</div><div class="r">Read more</div></div><span class="ph" style="right:0;background:linear-gradient(135deg,#2a8a3a,#e0c030,#c8a080)" role="img" aria-label="Presenter with a trophy poster"></span></div>
<div class="news" style="top:1854px"><div class="txt" style="left:16px"><div class="t" style="margin-top:0">Lorem ipsum dolor amet</div><div class="d" style="margin-top:8px">JUL 10, 2014</div><div class="r">Read more</div></div><span class="ph" style="right:0;background:linear-gradient(135deg,#2a6a8a,#c8b070,#2a2a2a)" role="img" aria-label="Officials on a stage"></span></div>
<div class="news" style="top:1950px"><div class="txt" style="left:16px"><div class="t" style="margin-top:0">Lorem ipsum dolor amet</div><div class="d" style="margin-top:8px">JUL 10, 2014</div><div class="r">Read more</div></div><span class="ph" style="right:0;background:linear-gradient(135deg,#1a1a2a,#7a3a7a,#3a5a2a)" role="img" aria-label="Night match action"></span></div>

<!-- The Sideline Chatter -->
<h2 class="sec-title" style="left:81px;top:2092px;font-size:20px">The Sideline Chatter</h2>
<div class="ph" style="left:81px;top:2126px;width:329px;height:177px;background:linear-gradient(135deg,#e0c030,#c89a7a,#2a7a3a)" role="img" aria-label="Young fans in yellow shirts with a player"></div>
<div class="feature-meta">Lorem ipsum <span>July 11, 2014</span></div>
<div class="feature-title">Lorem ipsum dolor sit amet, coctetur adipiscing elit</div>
<div class="feature-tags"><span class="tag">Top Sideline</span><span class="tag dark">Lifestyle</span></div>
<p class="feature-text">Donec non interdum risus. Duis porta luctus mi eget porta. Morbi lacinia neque sit amet vehicula tum</p>

<div class="post" style="top:2126px"><span class="ph" style="background:linear-gradient(135deg,#e0c030,#c89a7a,#2a7a3a)" role="img" aria-label="Fans in yellow"></span><h5 class="hl">Lorem ipsum dolor sit amet, consectetur</h5><div class="by">Kickoffwriter, July 10, 2014</div></div>
<div class="post" style="top:2217px"><span class="ph" style="background:linear-gradient(135deg,#e0c030,#2a7a3a,#c89a7a)" role="img" aria-label="Fans in yellow"></span><h5>Lorem ipsum dolor sit amet, consectetur adipi</h5><div class="by">Kickoffwriter, July 10, 2014</div></div>
<div class="post" style="top:2307px"><span class="ph" style="background:linear-gradient(135deg,#c89a7a,#e0c030,#2a4a9a)" role="img" aria-label="Fans in the stands"></span><h5>Lorem ipsum dolor sit amet</h5><div class="by">Kickoffwriter, July 10, 2014</div></div>
<div class="post" style="top:2397px"><span class="ph" style="background:linear-gradient(135deg,#2a7a3a,#c83a3a,#e0c030)" role="img" aria-label="Fans with flags"></span><h5>Lorem ipsum dolor sit amet, consectetur</h5><div class="by">Kickoffwriter, July 10, 2014</div></div>

<div class="abs ad" role="img" aria-label="Games console advertisement"><div class="console"></div><h6>Play beyond<br>the pitch</h6><small>Nova Console</small></div>
<div class="ph" style="left:800px;top:2316px;width:319px;height:162px;background:linear-gradient(135deg,#1a2a4a,#c8a030,#c83a3a 70%,#2a2a3a)" role="img" aria-label="Opening ceremony performers on stage"></div>

<footer class="abs footer">
  <div class="crumbs"><a class="hl">Home</a> / <a>About us</a> / <a>Tournaments</a> / <a>Contacts</a></div>
  <div class="foot-brand">Sideline Chatter</div>
  <div class="foot-mark"></div>
  <div class="copy">© 2014 | Privacy Policy</div>
  <ul class="fcol" style="left:538px"><li class="hl">News</li><li>Tournaments</li><li>Teams</li><li>Training</li></ul>
  <ul class="fcol" style="left:771px"><li>Equipment</li><li>Recruiting</li><li>Recruiting Camps</li><li>Services</li></ul>
  <ul class="fcol" style="left:1022px"><li>Calendar</li><li>Clinics</li><li>Photo Album</li><li>Our Sponsors</li></ul>
</footer>

</body>
</html>
```